Online shopping portal - Business Card Design

Brightcart.com.au is a complete shopping experience. Search, compare & buy items from partnered stores & receive cashbash for your purchases and referrals.
Mission
Our mission is to provide a system for entrepreneurs to create an ongoing income, while providing consumers worldwide with a better way to shop.
A product brokerage and Internet marketing company that specialises in One-to-One Marketing, Velora Oceania is a subsidiary of Velora Continental Holdings, Inc.
With more than 3 million Preferred Customers and 180,000 Customer Managers worldwide, Velora Continental has generated over $3 billion USD in accumulated retail sales. The Company employs more than 675 people globally with international operations in Australia, United States, Canada, Taiwan, Hong Kong, Mexico & Singapore
Through revolutionary technology and the one-to-one marketing and social shopping Velora Oceania are leveraging the Internet with the power of people to create the economy of the future.
By providing online shoppers with the products and services they want and need — backed by the Company’s people power — Velora Oceania is fast becoming the World Wide Web’s ultimate online shopping destination.
As a result, we are changing the way people shop and changing the economic paradigm where anyone can become financially independent by creating their own economy — Rooted in Goods. Driven by Folks®.
Description
Welcome to a new kind of comparison shopping site where you get PAID cashback to shop!
Simply create an account to start accumulating cash backs each time you make purchases across hundreds of trusted Partner Stores and thousands of your favorite brands through our convenient MonoBag® for one stop shopping.
All merchant stores are backed by BUYNEST.COM's 100% satisfaction guarantee.

Updates
Project Deadline Extended
Reason: Hi all,  I am extending the deadline as i'm going to be away for my birthday (and may not have time to check before the current deadline anyway)  I figure that the more time i give you the better.

Industry/Entity Type
Online Shopping
Contact Information for Business Card
Business Name: Brightcart.com.au
website: www.brightcart.com.au
Facebook: www.facebook.com/brightcart.com.au.
Email: info@brightcart.com.au
Phone: Quin on 0438 72 15 94
Requirements
Nice to have
- Create a Brightcart logo

```html
<!DOCTYPE html>
<html lang="en">
<head>
<meta charset="utf-8">
<title>Brightcart.com.au – Business Card</title>
<link rel="stylesheet" href="https://fonts.googleapis.com/css2?family=Open+Sans:wght@400;600;700&display=swap">
<style>
  :root {
    --backdrop: #e9e6e1;
    --card-white: #fbfbfb;
    --card-white-edge: #e2e2e2;
    --ink-dark: #4a4a4a;
    --ink-mid: #6d6d6d;
    --ink-soft: #9a9a9a;
    --accent: #2fa7d9;
    --accent-deep: #1687c3;
    --accent-light: #49c6e6;
    --band-grey: #808080;
    --swoosh: #8d8d8d;
  }
  * { box-sizing: border-box; margin: 0; padding: 0; }
  html, body { width: 1200px; height: 1023px; overflow: hidden; }
  body {
    background: var(--backdrop);
    font-family: "Open Sans", Arial, sans-serif;
    position: relative;
  }
  .card {
    position: absolute;
    width: 560px;
    height: 340px;
    border-radius: 26px;
    overflow: hidden;
    box-shadow: 0 10px 28px rgba(0,0,0,0.18);
  }

  /* Front */
  .card--front {
    left: 60px; top: 110px;
    background: linear-gradient(160deg, #ffffff 0%, var(--card-white) 60%, var(--card-white-edge) 100%);
  }
  .card__swoosh { position: absolute; inset: 0; }
  .brand {
    position: absolute;
    display: flex; align-items: center; gap: 10px;
    font-size: 26px; font-weight: 400; letter-spacing: 0.2px;
    white-space: nowrap;
  }
  .brand__dot {
    width: 32px; height: 32px; border-radius: 50%;
    background: var(--ink-dark);
  }
  .card--front .brand { left: 30px; top: 30px; color: var(--accent); }

  .identity {
    position: absolute; right: 32px; top: 70px;
    text-align: right; color: var(--ink-dark); white-space: nowrap;
  }
  .identity__name { font-size: 19px; font-weight: 700; }
  .identity__role { font-size: 13px; font-weight: 400; color: var(--ink-soft); }
  .identity__sep { color: var(--ink-mid); font-weight: 400; margin: 0 4px; }

  .contacts {
    position: absolute; right: 32px; top: 108px;
    list-style: none; font-size: 12.5px; color: var(--ink-mid);
  }
  .contacts li { display: flex; align-items: center; justify-content: flex-end; gap: 8px; height: 21px; white-space: nowrap; }
  .contacts__mark {
    width: 11px; height: 11px; border-radius: 2px; background: var(--accent);
    order: -1;
  }

  .pillars {
    position: absolute; right: 40px; bottom: 28px; width: 270px;
  }
  .pillars__icons { display: flex; justify-content: space-between; padding: 0 12px 8px; }
  .pillars__icons svg { width: 22px; height: 22px; }
  .pillars__rule { height: 1px; background: #c9c9c9; margin-bottom: 6px; }
  .pillars__text { font-size: 14px; color: var(--ink-mid); text-align: center; white-space: nowrap; }

  /* Back */
  .card--back {
    left: 580px; top: 560px;
    background: radial-gradient(ellipse at 60% 30%, var(--accent-light) 0%, var(--accent) 50%, var(--accent-deep) 100%);
  }
  .card--back .brand { left: 40px; top: 46px; color: var(--ink-dark); font-size: 34px; }
  .card--back .brand__dot { width: 40px; height: 40px; }
  .tagline-band {
    position: absolute; left: 300px; right: 0; bottom: 40px; height: 36px;
    background: var(--band-grey);
    display: flex; align-items: center; padding-left: 22px;
    color: #f2f2f2; font-size: 15px; letter-spacing: 1.5px; white-space: nowrap;
  }
</style>
</head>
<body>

  <section class="card card--front" aria-label="Business card front">
    <svg class="card__swoosh" viewBox="0 0 560 340" aria-hidden="true">
      <path d="M0 322 Q 200 60 560 22 L560 26 Q 210 76 0 340 Z" fill="var(--swoosh)" opacity="0.85"/>
      <path d="M60 340 Q 250 110 560 52" fill="none" stroke="#d6d6d6" stroke-width="1"/>
    </svg>

    <div class="brand"><span class="brand__dot"></span><span>Brightcart.com.au</span></div>

    <div class="identity">
      <span class="identity__name">Daniel Reeve</span><span class="identity__sep">|</span><span class="identity__role">Director</span>
    </div>

    <ul class="contacts">
      <li><span>Quin on 0438 72 15 94</span><span class="contacts__mark"></span></li>
      <li><span>info@brightcart.com.au</span><span class="contacts__mark"></span></li>
      <li><span>www.brightcart.com.au</span><span class="contacts__mark"></span></li>
      <li><span>/brightcart.com.au</span><span class="contacts__mark"></span></li>
    </ul>

    <div class="pillars">
      <div class="pillars__icons">
        <svg viewBox="0 0 24 24" aria-label="Search"><circle cx="10" cy="10" r="6" fill="none" stroke="var(--accent)" stroke-width="2.5"/><line x1="14.5" y1="14.5" x2="21" y2="21" stroke="var(--accent)" stroke-width="3" stroke-linecap="round"/></svg>
        <svg viewBox="0 0 24 24" aria-label="Compare"><rect x="2" y="6" width="9" height="12" rx="2" fill="none" stroke="var(--accent)" stroke-width="2"/><rect x="13" y="6" width="9" height="12" rx="2" fill="none" stroke="var(--accent)" stroke-width="2"/></svg>
        <svg viewBox="0 0 24 24" aria-label="Buy"><path d="M2 4h4l3 11h11l2-8H7" fill="none" stroke="var(--accent)" stroke-width="2.2" stroke-linejoin="round"/><circle cx="10" cy="19.5" r="1.8" fill="var(--accent)"/><circle cx="18" cy="19.5" r="1.8" fill="var(--accent)"/></svg>
        <svg viewBox="0 0 24 24" aria-label="Earn"><circle cx="12" cy="12" r="10" fill="none" stroke="var(--accent)" stroke-width="2"/><text x="12" y="16.5" text-anchor="middle" font-family="Open Sans, Arial, sans-serif" font-size="13" font-weight="700" fill="var(--accent)">$</text></svg>
      </div>
      <div class="pillars__rule"></div>
      <p class="pillars__text">Search • Compare • Buy • Earn</p>
    </div>
  </section>

  <section class="card card--back" aria-label="Business card back">
    <div class="brand"><span class="brand__dot"></span><span>Brightcart.com.au</span></div>
    <div class="tagline-band">Get paid to shop</div>
  </section>

</body>
</html>
```